Professional finish needed to powerpoint slides

I am pitching my business for investment and have two pages as part of the business plan called the 'Quillmarsh Orbit' and the 'Forged at Brackenmoor Orbit'.
They are basically visual one page plans to help investors see if the business is worth investing in or not. You only need to take the pages with the diagram in, so 2 pages in total.
The Orbit can be given an edge to make it look info graphic style.
Good luck

```html
<!DOCTYPE html>
<html lang="en">
<head>
<meta charset="utf-8">
<title>Quillmarsh Orbit</title>
<link href="https://fonts.googleapis.com/css2?family=Open+Sans:wght@400;600;700&display=swap" rel="stylesheet">
<style>
  :root {
    --stage: #2a2a2a;
    --sheet: #fafafa;
    --disc: #ffffff;
    --gap: #e7e7e7;
    --rule: #dcdcdc;
    --green: #3f9b48;
    --green-text: #4a9f3f;
    --ink: #4b4b4b;
    --label: #555555;
  }
  html, body {
    margin: 0;
    width: 1200px;
    height: 1000px;
    overflow: hidden;
    background: var(--stage);
    font-family: "Open Sans", Arial, sans-serif;
  }
  .orbit-sheet {
    position: absolute;
    top: 78px;
    left: 0;
    width: 1200px;
    height: 844px;
    display: block;
  }
  .sheet-bg { fill: var(--sheet); }
  .brand-name { fill: var(--green); font-size: 40px; font-weight: 600; letter-spacing: -0.5px; }
  .disc { fill: var(--disc); stroke: var(--rule); stroke-width: 1.5; }
  .ring { fill: none; stroke: var(--rule); stroke-width: 1; }
  .ring-on-band { fill: none; stroke: #ffffff; stroke-width: 1.5; }
  .divider { stroke: var(--gap); stroke-width: 6; }
  .year-band { fill: var(--green); }
  .hub { fill: url(#hubFill); stroke: #ffffff; stroke-width: 4; }
  .hub-edge { fill: none; stroke: #cfcfcf; stroke-width: 1; }
  .cell { font-size: 9.5px; text-anchor: middle; }
  .cell-grey { fill: var(--ink); }
  .cell-green { fill: var(--green-text); }
  .cell-small { font-size: 8.4px; }
  .year { fill: #ffffff; font-size: 12px; font-weight: 700; text-anchor: middle; }
  .spoke-label { font-size: 15px; text-anchor: middle; }
  .spoke-label.is-green { fill: var(--green-text); }
  .spoke-label.is-grey { fill: var(--label); }
  .leader { fill: none; stroke: #666666; stroke-width: 1; stroke-dasharray: 2 2; }
  .objectives-box { fill: url(#boxFill); stroke: #d0d0d0; stroke-width: 1; }
  .objectives-title { fill: var(--green-text); font-size: 15px; font-weight: 700; text-anchor: middle; }
</style>
</head>
<body>
<svg class="orbit-sheet" viewBox="105 150 985 693" xmlns="http://www.w3.org/2000/svg">
  <defs>
    <radialGradient id="hubFill" cx="45%" cy="40%" r="65%">
      <stop offset="0" stop-color="#4fb05a"/>
      <stop offset="1" stop-color="#2f8a3e"/>
    </radialGradient>
    <linearGradient id="boxFill" x1="0" y1="0" x2="0" y2="1">
      <stop offset="0" stop-color="#f7f7f7"/>
      <stop offset="1" stop-color="#e3e3e3"/>
    </linearGradient>
    <filter id="discShadow" x="-10%" y="-10%" width="120%" height="120%">
      <feDropShadow dx="0" dy="2" stdDeviation="3" flood-color="#000" flood-opacity="0.18"/>
    </filter>
  </defs>

  <rect class="sheet-bg" x="105" y="150" width="985" height="693"/>

  <!-- Brand name -->
  <g class="brand">
    <text class="brand-name" x="118" y="218">Quillmarsh</text>
  </g>

  <!-- Orbit disc -->
  <g class="orbit">
    <circle class="disc" cx="672" cy="487" r="330" filter="url(#discShadow)"/>
    <path class="year-band" d="M672,487 L980,369 A330,330 0 0 1 998,438 Z"/>
    <circle class="ring" cx="672" cy="487" r="118"/>
    <circle class="ring" cx="672" cy="487" r="210"/>
    <circle class="ring" cx="672" cy="487" r="265"/>
    <path class="ring-on-band" d="M782,445 A118,118 0 0 1 789,471"/>
    <path class="ring-on-band" d="M868,412 A210,210 0 0 1 880,456"/>
    <path class="ring-on-band" d="M919,392 A265,265 0 0 1 934,448"/>

    <g class="dividers">
      <line class="divider" x1="672" y1="487" x2="570" y2="173"/>
      <line class="divider" x1="672" y1="487" x2="712" y2="159"/>
      <line class="divider" x1="672" y1="487" x2="861" y2="217"/>
      <line class="divider" x1="672" y1="487" x2="980" y2="369"/>
      <line class="divider" x1="672" y1="487" x2="998" y2="438"/>
      <line class="divider" x1="672" y1="487" x2="949" y2="667"/>
      <line class="divider" x1="672" y1="487" x2="832" y2="776"/>
      <line class="divider" x1="672" y1="487" x2="483" y2="757"/>
      <line class="divider" x1="672" y1="487" x2="358" y2="589"/>
      <line class="divider" x1="672" y1="487" x2="344" y2="452"/>
      <line class="divider" x1="672" y1="487" x2="389" y2="317"/>
    </g>

    <circle class="hub-edge" cx="672" cy="487" r="58"/>
    <circle class="hub" cx="672" cy="487" r="54"/>

    <!-- Years -->
    <g class="years">
      <text class="year" transform="translate(755,469) rotate(-14.75)">2013</text>
      <text class="year" transform="translate(831,449) rotate(-14.75)">2014</text>
      <text class="year" transform="translate(901,431) rotate(-14.75)">2015</text>
      <text class="year" transform="translate(959,415) rotate(-14.75)">2016</text>
    </g>

    <!-- Net profit -->
    <g class="cell cell-green">
      <text x="664" y="404">£3,179</text>
      <text x="656" y="327">£91k</text>
      <text x="649" y="254">£150k</text>
      <text x="643" y="194">£300k</text>
    </g>

    <!-- Revenue -->
    <g class="cell cell-grey">
      <text class="cell-small" transform="translate(703,400) rotate(8)"><tspan x="0" dy="0">£179,175</tspan><tspan x="0" dy="10">(100k</tspan><tspan x="0" dy="10">Swr)</tspan></text>
      <text transform="translate(731,337) rotate(21)">£300k</text>
      <text transform="translate(757,269) rotate(21)">£500k</text>
      <text transform="translate(778,213) rotate(21)">£1m</text>
    </g>

    <!-- Subscribers -->
    <g class="cell cell-green">
      <text transform="translate(740,437) rotate(55)">35</text>
      <text transform="translate(801,389) rotate(-55)">104 @ £299</text>
      <text transform="translate(859,344) rotate(-55)">209 @ £299</text>
      <text transform="translate(906,307) rotate(-55)">418 @ £299</text>
    </g>

    <!-- Market segments -->
    <g class="cell cell-grey cell-small">
      <text transform="translate(832,521) rotate(-78)"><tspan x="0" dy="-15">(Avoid PR Market)</tspan><tspan x="0" dy="10">London/B'ham Tech</tspan><tspan x="0" dy="10">Govt Corp Suppliers</tspan><tspan x="0" dy="10">Mkt Global Private Biz</tspan></text>
      <text transform="translate(904,536) rotate(-78)"><tspan x="0" dy="-15">Diversification,</tspan><tspan x="0" dy="10">Agency Market</tspan><tspan x="0" dy="10">(criteria robust product)</tspan><tspan x="0" dy="10">Top 100 Companies</tspan><tspan x="0" dy="10">To Work For</tspan></text>
      <text transform="translate(962,549) rotate(-78)"><tspan x="0" dy="-2">Planned Evolution</tspan><tspan x="0" dy="10">with Markets</tspan></text>
    </g>

    <!-- Product mix -->
    <g class="cell cell-green">
      <text class="cell-small" transform="translate(731,550) rotate(-55)"><tspan x="0" dy="-7">Software 56%</tspan><tspan x="0" dy="10">(Mkg PR, Marsh Blast,</tspan><tspan x="0" dy="10">Rpot Ad – 44%)</tspan></text>
      <text transform="translate(784,607) rotate(-55)"><tspan x="0" dy="-2">Software 90%,</tspan><tspan x="0" dy="11">Marsh Blast 10%</tspan></text>
      <text transform="translate(834,663) rotate(-43)">100%</text>
      <text transform="translate(875,707) rotate(-43)">100%</text>
    </g>

    <!-- Marketing -->
    <g class="cell cell-grey">
      <text class="cell-small" x="680" y="615"><tspan x="680" dy="0">Webinars, Pellow, Awareness</tspan><tspan x="680" dy="10.5">London M'chster, Develop</tspan><tspan x="680" dy="10.5">Brand /Val. Prop.,Lead Gen.</tspan><tspan x="680" dy="10.5">Campaigns, Searchly Ad, e-shots,</tspan><tspan x="680" dy="10.5">Target Regions, Mystery Shopping,</tspan><tspan x="680" dy="10.5">Online Demos, Introduce A Pro-active Sales</tspan><tspan x="680" dy="10.5">Process &amp; Monitoring, Company Product</tspan><tspan x="680" dy="10.5">“In House” Capabilities – Identify Through Media</tspan><tspan x="680" dy="10.5">(Research) Database AIM Listed plc's</tspan></text>
      <text x="664" y="728"><tspan x="664" dy="0">App.,In House Developers, In House Media,</tspan><tspan x="664" dy="11">Data Control, Social Network,</tspan><tspan x="664" dy="11">Journalist Bloggers</tspan></text>
      <text x="672" y="782"><tspan x="672" dy="0">Review &amp; Continual Adaption Related to</tspan><tspan x="672" dy="11">Market &amp; New Technologies</tspan></text>
    </g>

    <!-- Direct sales -->
    <g class="cell cell-green">
      <text class="cell-small" transform="translate(540,585) rotate(53.5)"><tspan x="0" dy="-20">10-20 plc's</tspan><tspan x="0" dy="10">Via Website &amp; Get</tspan><tspan x="0" dy="10">Contacts Get</tspan><tspan x="0" dy="10">1 in Plc, Mkting,</tspan><tspan x="0" dy="10">Comms, HR</tspan><tspan x="0" dy="10">FD, MD, Chair</tspan></text>
      <text transform="translate(481,628) rotate(53.5)"><tspan x="0" dy="-8">Establish “Quillmarsh”</tspan><tspan x="0" dy="11">Way – Implement,</tspan><tspan x="0" dy="11">Continually Monitor &amp; Review</tspan></text>
      <text transform="translate(433,664) rotate(53.5)">As Year 2</text>
    </g>

    <!-- Operations -->
    <g class="cell cell-grey cell-small">
      <text transform="translate(509,504) rotate(-96)"><tspan x="0" dy="-22">Resellers, Franchise,</tspan><tspan x="0" dy="10">Partners Europe,</tspan><tspan x="0" dy="10">Manchester,</tspan><tspan x="0" dy="10">London,</tspan><tspan x="0" dy="10">Global</tspan><tspan x="0" dy="10">Markets Pull</tspan></text>
      <text transform="translate(436,512) rotate(-96)" style="font-size:9.5px"><tspan x="0" dy="-8">Consolidate UK, More</tspan><tspan x="0" dy="11">Global Markets</tspan><tspan x="0" dy="11">(planned)</tspan></text>
    </g>

    <!-- Skills / training -->
    <g class="cell cell-green">
      <text transform="translate(517,435) rotate(-71.5)"><tspan x="0" dy="-2">Bring in skills</tspan><tspan x="0" dy="11">(buy in)</tspan></text>
    </g>

    <!-- People -->
    <g class="cell cell-grey">
      <text class="cell-small" transform="translate(618,420) rotate(38.5)"><tspan x="0" dy="-2">1 Sales</tspan><tspan x="0" dy="10">Person</tspan></text>
      <text transform="translate(570,362) rotate(38.5)">2 Sales Person</text>
      <text class="cell-small" transform="translate(524,301) rotate(-51.5)"><tspan x="0" dy="-12">In house Media x 2,</tspan><tspan x="0" dy="10">Team – Chirper –</tspan><tspan x="0" dy="10">2 Sales People</tspan><tspan x="0" dy="10">London/Manchester</tspan></text>
      <text class="cell-small" transform="translate(487,254) rotate(-51.5)"><tspan x="0" dy="-7">Chief Technical Officer,</tspan><tspan x="0" dy="10">4 Sales People</tspan><tspan x="0" dy="10">London/Manchester</tspan></text>
    </g>
  </g>

  <!-- Spoke labels -->
  <g class="spoke-labels">
    <text class="spoke-label is-grey" x="437" y="230">People</text>
    <polyline class="leader" points="405,237 466,237 478,226"/>

    <text class="spoke-label is-green" x="593" y="165">Net Profit</text>
    <polyline class="leader" points="548,173 638,173 648,160"/>

    <text class="spoke-label is-grey" x="833" y="182">Revenue</text>
    <polyline class="leader" points="780,180 795,189 872,189"/>

    <text class="spoke-label is-green" x="978" y="274">Subscribers</text>
    <polyline class="leader" points="918,272 928,282 1030,282"/>

    <text class="spoke-label is-grey" x="1034" y="503">Market</text>
    <text class="spoke-label is-grey" x="1045" y="521">Segments</text>
    <polyline class="leader" points="1001,505 1008,528 1088,528"/>

    <text class="spoke-label is-green" x="993" y="701">Product Mix</text>
    <polyline class="leader" points="928,692 940,709 1045,709"/>

    <text class="spoke-label is-grey" x="698" y="835">Marketing</text>
    <polyline class="leader" points="640,815 655,841 740,841"/>

    <text class="spoke-label is-green" x="355" y="694">Direct Sales</text>
    <polyline class="leader" points="300,702 395,702 408,685"/>

    <text class="spoke-label is-grey" x="292" y="521">Operations</text>
    <polyline class="leader" points="248,529 336,529 344,520"/>

    <text class="spoke-label is-green" x="296" y="369">Skills/ Training</text>
    <polyline class="leader" points="238,376 365,376 375,352"/>
  </g>

  <!-- Objectives -->
  <g class="objectives">
    <rect class="objectives-box" x="112" y="706" width="171" height="126" rx="3"/>
    <text class="objectives-title" x="198" y="726">Objectives</text>
  </g>
</svg>
</body>
</html>
```